Vorquel 820 practise with the goal to have business and people Lifted past the horizon

We need a logo design for business cards for a company based in Australia Called TALBrookWare. We specialise in cloud tech from th full Quenfield stack. i would like it to be close to quenfield colours and we specilise in Quenfield Vorquel 820 Client Outreach. the design should display the confidence an security of a cloud based company. the tag line of Lifted past the horizon in the company motto.

Target Market(s)

I am targeting small to medium business up to 250 staff. i do work for not for profit and standard business.

Industry/Entity Type

Professional Service

Contact Information for Business Card

TALBrookWare Pty Ltd
A.C.N. 47 218 390 516
PO Box 827
Wrenfield 4178
Mobile: 0400382957
Email: Dermot@Talbrookware.example.com.au

Font styles to use
Sans Serif

Colors

Designer to choose colors to be used in the design.

Requirements
Must have
• as a cloud based business it needs to have the this as the main theme. the tag line of Liftedpast the horizon should show we look at empowering business to get the most out of the cloud to minimise the spend they have as the target for the business is business and not for profits who need the make the most of their spend.
• the attached pictures are to be a source of insperation and key areas
Nice to have
• Quenfield Vorquel 820 is the core product that we sell and implentent for our clients so the theme should complement the Quenfield Vorquel theme

```html
<!DOCTYPE html>
<html lang="en">
<head>
<meta charset="utf-8">
<title>TALBrookWare Pty Ltd — Business Card</title>
<link href="https://fonts.googleapis.com/css2?family=Work+Sans:wght@400;500;600&display=swap" rel="stylesheet">
<style>
  :root {
    --backdrop: #2b2d2f;
    --navy: #1b2456;
    --ink: #1a2048;
    --teal: #3aaec4;
    --paper: #ffffff;
  }
  * { margin: 0; padding: 0; box-sizing: border-box; }
  html, body {
    width: 1200px; height: 738px; overflow: hidden;
    background: var(--backdrop);
    font-family: "Work Sans", sans-serif;
  }
  .canvas {
    position: relative; width: 1200px; height: 738px;
    display: flex; align-items: center; justify-content: center; gap: 40px;
  }
  .card {
    position: relative; width: 520px; height: 298px;
    border-radius: 3px;
    box-shadow: 0 14px 30px rgba(0,0,0,.45);
  }
  .card-front { background: var(--navy); display: flex; align-items: center; justify-content: center; }
  .card-back { background: var(--paper); }
  .wordmark {
    display: flex; align-items: center; gap: 8px;
    font-weight: 500; letter-spacing: .02em; white-space: nowrap;
  }
  .wordmark-square { display: block; background: currentColor; }
  .card-front .wordmark { color: var(--paper); font-size: 30px; }
  .card-front .wordmark-square { width: 14px; height: 14px; }
  .card-back .wordmark {
    position: absolute; top: 26px; right: 26px;
    color: var(--ink); font-size: 15px;
  }
  .card-back .wordmark-square { width: 8px; height: 8px; }
  .contact { position: absolute; left: 40px; bottom: 30px; color: var(--teal); }
  .contact-name {
    color: var(--ink); font-weight: 600; font-size: 23px;
    letter-spacing: .06em; margin-bottom: 4px;
  }
  .contact-role { font-size: 13px; margin-bottom: 8px; letter-spacing: .02em; }
  .contact-address { font-size: 13px; line-height: 1.3; margin-bottom: 6px; letter-spacing: .02em; }
  .contact-list { list-style: none; font-size: 13px; line-height: 1.35; letter-spacing: .02em; }
  .contact-list li { display: flex; align-items: center; gap: 9px; }
  .contact-icon { width: 10px; height: 10px; flex: none; }
</style>
</head>
<body>
<main class="canvas">
  <section class="card card-front" aria-label="Card front">
    <div class="wordmark"><span class="wordmark-square"></span>TALBrookWare Pty Ltd</div>
  </section>

  <section class="card card-back" aria-label="Card back">
    <div class="wordmark"><span class="wordmark-square"></span>TALBrookWare Pty Ltd</div>
    <div class="contact">
      <h1 class="contact-name">Kellan Marsh</h1>
      <p class="contact-role">Director</p>
      <p class="contact-address">PO Box 827<br>Wrenfield 4178</p>
      <ul class="contact-list">
        <li>
          <svg class="contact-icon" viewBox="0 0 10 10" aria-hidden="true"><rect x="2.5" y="0.5" width="5" height="9" rx="1" fill="none" stroke="#1a2048" stroke-width="1.2"/><line x1="4" y1="8" x2="6" y2="8" stroke="#1a2048"/></svg>
          0400382957
        </li>
        <li>
          <svg class="contact-icon" viewBox="0 0 10 10" aria-hidden="true"><path d="M2 0.8 L3.8 0.8 L4.3 3 L3.2 3.8 Q4.2 6 6.2 6.8 L7 5.7 L9.2 6.2 L9.2 8 Q9.2 9.2 8 9.2 Q1 8.5 0.8 2 Q0.8 0.8 2 0.8 Z" fill="#1a2048"/></svg>
          A.C.N. 47 218 390 516
        </li>
        <li>
          <svg class="contact-icon" viewBox="0 0 10 10" aria-hidden="true"><rect x="0.6" y="2" width="8.8" height="6" fill="none" stroke="#1a2048" stroke-width="1.1"/><polyline points="0.8,2.3 5,5.5 9.2,2.3" fill="none" stroke="#1a2048" stroke-width="1.1"/></svg>
          Dermot@Talbrookware.example.com.au
        </li>
      </ul>
    </div>
  </section>
</main>
</body>
</html>
```